Ad Banner for Expert Web Board

This banner is used in "Lantern Quay" web site. This web site provides a single place for all employees to ask questions related to work. There will be dedicated subject matter experts to respond to all questions. The web site also provides "Maple Ledger" where employee can see the list of all experts in the company.
1. Banner size: 940x380
2. Business background: Provides maintenance, design and engineering, construction, machinery operation, material procurement and production management services for petrochemical and refinery business
3. We would like to see designs that
- Promote the ask questions in "Lantern Quay" system
- Promote that company has experts in the areas of "Maintenance and Engineering" and can be found in "Maple Ledger"
- Encourage employees to advocate himself to be an expert by sending an email to a specific email address.
- Do not include picture of real people in the banner

```html
<!DOCTYPE html>
<html lang="en">
<head>
<meta charset="utf-8">
<title>Lantern Quay – Banner</title>
<link href="https://fonts.googleapis.com/css2?family=Montserrat:wght@800;900&family=Open+Sans:wght@400;600&display=swap" rel="stylesheet">
<style>
  :root {
    --sky-deep: #1592d4;
    --sky-mid: #3aa9de;
    --sky-light: #9fd6ee;
    --glow: #e9f6fc;
    --white: #ffffff;
    --pill-yellow: #f7ef3c;
    --pill-text: #1b8ccb;
    --icon-orange: #ec5a2c;
    --hero-shirt: #f3f3f1;
    --hero-cape: #e8643c;
    --divider: rgba(255,255,255,0.55);
  }
  * { margin: 0; padding: 0; box-sizing: border-box; }
  html, body { width: 1200px; height: 485px; overflow: hidden; background: var(--sky-deep); }

  .banner {
    position: relative;
    width: 1200px;
    height: 485px;
    overflow: hidden;
    background:
      radial-gradient(circle at 260px 170px, var(--glow) 0%, var(--sky-light) 22%, var(--sky-mid) 48%, var(--sky-deep) 78%);
    font-family: "Open Sans", Arial, sans-serif;
    color: var(--white);
  }

  .hero-figure {
    position: absolute;
    left: 80px;
    top: 20px;
    width: 340px;
    height: 465px;
    border-radius: 150px 150px 40px 40px;
    background: linear-gradient(170deg, var(--hero-shirt) 0%, #f5cfa4 45%, var(--hero-cape) 100%);
    opacity: 0.85;
  }

  .divider {
    position: absolute;
    left: 600px;
    top: 45px;
    width: 2px;
    height: 395px;
    background: linear-gradient(to bottom, transparent, var(--divider) 15%, var(--divider) 85%, transparent);
    box-shadow: 2px 0 3px rgba(0,40,80,0.25);
  }

  .headline {
    position: absolute;
    left: 624px;
    top: 34px;
    font-family: "Montserrat", Arial, sans-serif;
    font-weight: 900;
    font-size: 80px;
    line-height: 66px;
    letter-spacing: -1px;
    text-transform: uppercase;
    text-shadow: 0 3px 4px rgba(0,50,90,0.35);
  }

  .tagline {
    position: absolute;
    left: 630px;
    top: 190px;
    font-size: 20px;
    line-height: 27px;
  }

  .directory-pill {
    position: absolute;
    left: 618px;
    top: 284px;
    width: 470px;
    height: 50px;
    border-radius: 25px;
    background: var(--pill-yellow);
    padding-left: 22px;
    font-family: "Montserrat", Arial, sans-serif;
    font-weight: 800;
    font-size: 31px;
    line-height: 50px;
    color: var(--pill-text);
    text-transform: uppercase;
  }

  .directory-icon {
    position: absolute;
    left: 1054px;
    top: 261px;
    width: 94px;
    height: 94px;
  }

  .invite-box {
    position: absolute;
    left: 634px;
    top: 334px;
    width: 434px;
    height: 96px;
    border: 1.5px solid rgba(255,255,255,0.85);
    border-top: none;
    border-radius: 0 0 8px 8px;
    padding: 12px 10px 0 9px;
    font-size: 19px;
    line-height: 24px;
  }
</style>
</head>
<body>
  <div class="banner">
    <div class="hero-figure" role="img" aria-label="Cartoon office superhero in white shirt, blue tie and orange cape, fist raised"></div>

    <div class="divider"></div>

    <h1 class="headline">Lantern<br>Quay</h1>

    <p class="tagline">Find a expert in Maintenance<br>and Engineering in the</p>

    <div class="directory-pill">Maple Ledger</div>

    <svg class="directory-icon" viewBox="0 0 94 94" aria-hidden="true">
      <circle cx="47" cy="47" r="46" fill="#ffffff"/>
      <circle cx="47" cy="47" r="38" fill="none" stroke="#d7e3ea" stroke-width="2"/>
      <circle cx="47" cy="47" r="34" fill="var(--icon-orange)"/>
      <rect x="33" y="28" width="28" height="38" rx="3" fill="none" stroke="#ffffff" stroke-width="3"/>
      <rect x="29" y="33" width="7" height="3" fill="#ffffff"/>
      <rect x="29" y="45" width="7" height="3" fill="#ffffff"/>
      <rect x="29" y="57" width="7" height="3" fill="#ffffff"/>
      <circle cx="48" cy="42" r="5" fill="#ffffff"/>
      <path d="M39 58 q9 -14 18 0 z" fill="#ffffff"/>
    </svg>

    <p class="invite-box">You can be an expert, send an email to<br>ask@lanternquay.com<br>and share your knowledge</p>
  </div>
</body>
</html>
```